Stationary for Velmo HPG, LLC
Company Name and slogan: Name: Velmo HPG, LLC and slogan "Moving in the Right Direction"
Stationary for Velmo HPG, LLC - Real Estate
Creative Brief
Use specific fonts
You can use the logo fonts or any fonts you deem creatively important.
Professional
Curtis Pellow
Solutions Specialist
41 Quarrington Court, Box 352 Fort Lee, NJ 07024
cpellow@velmohpg-example.com
http://www.velmohpg-example.com
The Logo can be moved to the side of the company name and slogan if needed. The 3 items below do not have to be on the front of the business card if it will take from the design. *1 is most important of the 3. *1. We Buy Houses, Help with Foreclosures, CALL NOW!!! 2. We provide real estate solutions 3. Working together to make a difference. Also on back of business cards the * is a bullet or whatever you think is needed.
Company Name and slogan: Name: Velmo HPG, LLC and slogan "Moving in the Right Direction" Benefits: * We give immediate debt relief * We stop foreclosure * We pay down your mortgage * We increase your equity * We save you marketing $$ * We will sell your house for you * We save you on Realtors commissions * We find you a buyer * We allow you to keep your tax breaks CALL NOW!!! 201-555-0186

```html
<!DOCTYPE html>
<html lang="en">
<head>
<meta charset="utf-8">
<title>Velmo HPG, LLC – Business Card</title>
<link href="https://fonts.googleapis.com/css2?family=Open+Sans:ital,wght@0,400;0,600;0,700;1,400;1,600&display=swap" rel="stylesheet">
<style>
  :root {
    --bg: #ecebe8;
    --blue: #3d8db3;
    --purple: #a2288f;
    --white: #ffffff;
    --ink: #4a4a4a;
    --ink-soft: #6b6b6b;
  }
  * { box-sizing: border-box; margin: 0; padding: 0; }
  html, body { width: 1200px; height: 901px; overflow: hidden; }
  body {
    background: var(--bg);
    font-family: "Open Sans", Arial, sans-serif;
    position: relative;
  }
  .card {
    position: absolute;
    width: 600px;
    height: 343px;
    border-radius: 22px;
    overflow: hidden;
    box-shadow: 0 6px 18px rgba(0,0,0,.18);
  }

  /* Back of card */
  .card-back { left: 60px; top: 100px; background: var(--blue); color: var(--white); }
  .card-back .brand { position: absolute; left: 40px; top: 112px; width: 230px; text-align: center; }
  .brand-mark { display: inline-block; width: 34px; height: 34px; background: var(--white); margin-bottom: 8px; }
  .card-back .brand-name { font-size: 40px; font-weight: 700; line-height: 1; white-space: nowrap; }
  .card-back .brand-llc { font-size: 13px; font-weight: 600; margin-top: 2px; }
  .card-back .brand-slogan { font-size: 15px; font-weight: 600; margin-top: 2px; white-space: nowrap; }
  .benefits { position: absolute; left: 310px; top: 30px; font-size: 13px; line-height: 19px; }
  .benefits h3 { font-size: 13px; font-weight: 400; letter-spacing: .5px; }
  .benefits ul { list-style: none; margin-top: 4px; }
  .benefits li { display: flex; align-items: center; gap: 8px; white-space: nowrap; }
  .benefits li svg { width: 11px; height: 11px; flex: none; }
  .call { margin-top: 12px; font-size: 13px; letter-spacing: .5px; }
  .call-phone { font-size: 19px; }

  /* Front of card */
  .card-front { left: 540px; top: 480px; background: var(--white); }
  .card-front .brand { position: absolute; left: 30px; top: 62px; width: 300px; text-align: center; }
  .card-front .brand-mark { background: var(--purple); }
  .card-front .brand-name { font-size: 50px; font-weight: 700; color: var(--blue); line-height: 1; white-space: nowrap; }
  .card-front .brand-llc { font-size: 14px; font-weight: 600; color: var(--blue); }
  .card-front .brand-slogan { font-size: 17px; font-weight: 700; color: var(--blue); border-top: 2px solid var(--blue); display: inline-block; padding-top: 2px; white-space: nowrap; }
  .tagline-band {
    position: absolute; left: 0; bottom: 42px; width: 405px; height: 38px;
    background: var(--blue); color: var(--white);
    font-size: 14px; font-style: italic; display: flex; align-items: center; padding-left: 18px; white-space: nowrap;
  }
  .contact { position: absolute; left: 380px; top: 52px; color: var(--ink); font-size: 12.5px; line-height: 18px; }
  .contact-name { color: var(--purple); font-size: 19px; font-weight: 600; line-height: 22px; }
  .contact-title { color: var(--ink-soft); font-size: 13px; }
  .contact-address { margin-top: 14px; width: 210px; }
  .contact-lines { list-style: none; margin-top: 14px; }
  .contact-lines li { display: flex; align-items: center; gap: 7px; white-space: nowrap; }
  .contact-lines svg { width: 12px; height: 12px; flex: none; }
  .contact-email { font-size: 12px; letter-spacing: -.1px; }
  .web-band {
    position: absolute; right: 0; bottom: 0; width: 280px; height: 38px;
    background: var(--purple); color: var(--white);
    font-size: 14px; letter-spacing: 1px; display: flex; align-items: center; justify-content: center; white-space: nowrap;
  }
</style>
</head>
<body>

<section class="card card-back">
  <div class="brand">
    <span class="brand-mark"></span>
    <div class="brand-name">Velmo HPG</div>
    <div class="brand-llc">LLC</div>
    <div class="brand-slogan">Moving in the right direction</div>
  </div>
  <div class="benefits">
    <h3>BENEFITS:</h3>
    <ul>
      <li><svg viewBox="0 0 12 12"><rect x=".5" y=".5" width="11" height="11" fill="none" stroke="#fff"/><path d="M2.5 6l2.5 2.5 4.5-5" fill="none" stroke="#fff" stroke-width="1.5"/></svg>We give immediate debt relief</li>
      <li><svg viewBox="0 0 12 12"><rect x=".5" y=".5" width="11" height="11" fill="none" stroke="#fff"/><path d="M2.5 6l2.5 2.5 4.5-5" fill="none" stroke="#fff" stroke-width="1.5"/></svg>We stop foreclosure</li>
      <li><svg viewBox="0 0 12 12"><rect x=".5" y=".5" width="11" height="11" fill="none" stroke="#fff"/><path d="M2.5 6l2.5 2.5 4.5-5" fill="none" stroke="#fff" stroke-width="1.5"/></svg>We pay down your mortgage</li>
      <li><svg viewBox="0 0 12 12"><rect x=".5" y=".5" width="11" height="11" fill="none" stroke="#fff"/><path d="M2.5 6l2.5 2.5 4.5-5" fill="none" stroke="#fff" stroke-width="1.5"/></svg>We increase your equity</li>
      <li><svg viewBox="0 0 12 12"><rect x=".5" y=".5" width="11" height="11" fill="none" stroke="#fff"/><path d="M2.5 6l2.5 2.5 4.5-5" fill="none" stroke="#fff" stroke-width="1.5"/></svg>We save you marketing $$</li>
      <li><svg viewBox="0 0 12 12"><rect x=".5" y=".5" width="11" height="11" fill="none" stroke="#fff"/><path d="M2.5 6l2.5 2.5 4.5-5" fill="none" stroke="#fff" stroke-width="1.5"/></svg>We will sell your house for you</li>
      <li><svg viewBox="0 0 12 12"><rect x=".5" y=".5" width="11" height="11" fill="none" stroke="#fff"/><path d="M2.5 6l2.5 2.5 4.5-5" fill="none" stroke="#fff" stroke-width="1.5"/></svg>We save you on Realtors commissions</li>
      <li><svg viewBox="0 0 12 12"><rect x=".5" y=".5" width="11" height="11" fill="none" stroke="#fff"/><path d="M2.5 6l2.5 2.5 4.5-5" fill="none" stroke="#fff" stroke-width="1.5"/></svg>We find you a buyer</li>
      <li><svg viewBox="0 0 12 12"><rect x=".5" y=".5" width="11" height="11" fill="none" stroke="#fff"/><path d="M2.5 6l2.5 2.5 4.5-5" fill="none" stroke="#fff" stroke-width="1.5"/></svg>We allow you to keep your tax breaks</li>
    </ul>
    <div class="call">CALL NOW!!!</div>
    <div class="call-phone">201-555-0186</div>
  </div>
</section>

<section class="card card-front">
  <div class="brand">
    <span class="brand-mark"></span>
    <div class="brand-name">Velmo HPG</div>
    <div class="brand-llc">LLC</div>
    <div class="brand-slogan">Moving in the right direction</div>
  </div>
  <div class="contact">
    <div class="contact-name">Curtis Pellow</div>
    <div class="contact-title">Solutions Specialist</div>
    <div class="contact-address">41 Quarrington Court, Box 352<br>Alder Bay, NJ 07915</div>
    <ul class="contact-lines">
      <li><svg viewBox="0 0 12 12"><path d="M1 4c0-2 2-3 5-3s5 1 5 3l-2 1-1-2H4L3 5zM3 6h6l1 5H2z" fill="#4a4a4a"/></svg>201-555-0186</li>
      <li><svg viewBox="0 0 12 12"><rect x="3" y="0.5" width="6" height="11" rx="1" fill="none" stroke="#4a4a4a"/><circle cx="6" cy="9.5" r=".8" fill="#4a4a4a"/></svg>201-555-0142</li>
      <li><svg viewBox="0 0 12 12"><rect x="1" y="5" width="10" height="6" fill="#4a4a4a"/><rect x="3" y="1" width="6" height="4" fill="none" stroke="#4a4a4a"/></svg>201-555-0186</li>
      <li class="contact-email"><svg viewBox="0 0 12 12"><rect x=".5" y="2.5" width="11" height="7" fill="none" stroke="#4a4a4a"/><path d="M.5 2.5L6 7l5.5-4.5" fill="none" stroke="#4a4a4a"/></svg>cpellow@velmohpg-example.com</li>
    </ul>
  </div>
  <div class="tagline-band">We Buy Houses, Help with Foreclosures, CALL NOW!!!</div>
  <div class="web-band">www.velmohpg-example.com</div>
</section>

</body>
</html>
```